We are in search of a new business card design for our business. We have a Mexican Grocery Store called Tortilla Grove Market, we would like to see that some have mexican design, but we are open to any type of designs.

Phone: to be announced
Fax: to be announced

Address is:
2415 Calloway Blvd
Bayfield, MD 21219

```html
<!DOCTYPE html>
<html lang="en">
<head>
<meta charset="utf-8">
<title>Tortilla Grove Market – Business Card</title>
<link rel="stylesheet" href="https://fonts.googleapis.com/css2?family=Roboto+Condensed:wght@300;400;700&display=swap">
<style>
  :root {
    --backdrop: #2a2a2a;
    --card-white: #ffffff;
    --card-orange: #fb8a10;
    --brand-red: #c0282e;
    --brand-green: #2f8a12;
    --title-orange: #f39a2a;
    --ink: #555555;
    --ink-light: #fff3e0;
  }
  * { box-sizing: border-box; margin: 0; padding: 0; }
  html, body {
    width: 1200px; height: 950px; overflow: hidden;
    background: var(--backdrop);
    font-family: "Roboto Condensed", sans-serif;
  }
  .canvas {
    position: relative; width: 1200px; height: 950px;
    display: flex; flex-direction: column; align-items: center;
    justify-content: center; gap: 50px;
  }
  .card {
    position: relative; width: 700px; height: 400px; overflow: hidden;
  }
  .card-front { background: var(--card-white); }
  .card-back { background: var(--card-orange); }

  .brand {
    position: absolute; display: flex; align-items: center; gap: 16px;
    white-space: nowrap;
  }
  .brand-dot {
    width: 44px; height: 44px; border-radius: 50%;
    background: var(--brand-red); flex: none;
  }
  .brand-name {
    font-weight: 700; color: var(--brand-red);
    text-transform: uppercase; letter-spacing: 1px; line-height: 1;
    white-space: nowrap;
  }
  .card-front .brand { top: 70px; right: 70px; }
  .card-front .brand-name { font-size: 34px; }

  .divider {
    position: absolute; left: 50px; right: 50px; top: 200px;
    height: 1px; background: var(--brand-red);
  }

  .contact {
    position: absolute; left: 50px; top: 232px; color: var(--ink);
  }
  .contact-name {
    font-size: 26px; font-weight: 400; color: var(--brand-red);
    text-transform: uppercase; letter-spacing: 0.5px;
  }
  .contact-title {
    font-size: 17px; color: var(--title-orange); margin-bottom: 16px;
  }
  .contact-line { font-size: 16px; font-weight: 300; line-height: 1.5; }
  .contact-line b { color: var(--brand-red); font-weight: 700; }

  .edge-band {
    position: absolute; left: 0; right: 0; bottom: 0; height: 16px;
    display: flex;
  }
  .edge-band span { flex: 1; }
  .edge-red { background: var(--brand-red); }
  .edge-green { background: var(--brand-green); }

  .card-back .brand {
    top: 50%; left: 50%; transform: translate(-50%, -50%);
  }
  .card-back .brand-dot { width: 56px; height: 56px; }
  .card-back .brand-name { font-size: 44px; color: var(--card-white); }

  .website {
    position: absolute; left: 34px; top: 50%;
    writing-mode: vertical-rl; transform: translateY(-50%) rotate(180deg);
    font-size: 14px; letter-spacing: 3px; color: var(--ink-light);
    white-space: nowrap;
  }
</style>
</head>
<body>
<main class="canvas">
  <section class="card card-front" aria-label="Card front">
    <div class="brand">
      <span class="brand-dot"></span>
      <span class="brand-name">Tortilla Grove Market</span>
    </div>
    <div class="divider"></div>
    <div class="contact">
      <p class="contact-name">Marco Ibarra</p>
      <p class="contact-title">President</p>
      <p class="contact-line">2415 Calloway Blvd, Bayfield, MD 21219</p>
      <p class="contact-line"><b>P</b> : 410 5520 1187&nbsp;&nbsp;<b>F</b> : 410 5520 1190</p>
    </div>
    <div class="edge-band"><span class="edge-red"></span><span class="edge-green"></span></div>
  </section>

  <section class="card card-back" aria-label="Card back">
    <p class="website">www.tortillagrove.com</p>
    <div class="brand">
      <span class="brand-dot"></span>
      <span class="brand-name">Tortilla Grove Market</span>
    </div>
  </section>
</main>
</body>
</html>
```